Economic Development Consulting needs killer brochure for National Civic Design Society Conference

Brightwater Advisors is an elite sponsor for the NCDS conference this year. Our Three service offerings for the event are
Economic Development Master Planning (and our proprietary approach)
Feasibility Studies and Site Options Analysis (also leverages our proprietary approach)
Resilience Assessment & Planning
Our slogan is Customized consulting for communities and community planners and Uncommon Insights — Aligning Resources to Opportunity

We need a square, trifold brochure, and we would like 3 posters, one dedicated to each of our service offerings, matching the brochure.

The NCDS conference site is http://www.ncdsfrontier.org/annual-conference
Updates

We have increased the budget for the brochure requested. The posters referenced int eh posting will be a separate project, offered to the designer who designs the brochure.

Reason: We are looking at adding some additional text.

Target Market(s)

Planners, Architects,

Industry/Entity Type

Consulting

Font styles to use
Sans Serif

Colors
0255a3

Requirements
Must have
• Square, trifold

```html
<!DOCTYPE html>
<html lang="en">
<head>
<meta charset="utf-8">
<title>Brightwater Advisors – Uncommon Insights Trifold</title>
<link rel="stylesheet" href="https://fonts.googleapis.com/css2?family=Saira+Condensed:wght@600;700&family=Open+Sans:wght@300;400;700&family=Crimson+Pro:wght@400&display=swap">
<style>
  :root {
    --brand-blue: #0255a3;
    --brand-blue-dark: #0a3f7c;
    --ink: #1d1d1d;
    --paper: #ffffff;
    --sepia-light: #e9dcc4;
    --sepia-mid: #b08e5c;
    --sepia-dark: #4a3620;
  }
  * { box-sizing: border-box; margin: 0; padding: 0; }
  html, body { width: 1200px; height: 1000px; overflow: hidden; background: var(--paper); }
  body { position: relative; font-family: "Open Sans", sans-serif; color: var(--ink); }

  .spread { position: absolute; left: 0; width: 1200px; height: 400px; background: var(--paper);
    box-shadow: 0 22px 22px -10px rgba(0,0,0,.45); overflow: hidden; }
  .spread--outside { top: 45px; }
  .spread--inside { top: 487px; }
  .panel { position: absolute; top: 0; height: 400px; }

  /* Outside spread */
  .photo-chess { left: 0; width: 400px;
    background: radial-gradient(ellipse at 65% 40%, var(--sepia-light) 0%, var(--sepia-mid) 55%, var(--sepia-dark) 100%); }
  .quote-box { position: absolute; left: 0; top: 67px; width: 267px; height: 131px;
    background: rgba(2,85,163,.88); padding: 14px 10px 0 20px; color: #fff; }
  .quote-box p { font-size: 13px; font-weight: 300; line-height: 17px; }
  .quote-box .author { margin-top: 9px; text-align: right; font-family: "Saira Condensed", sans-serif;
    font-weight: 700; font-size: 11px; letter-spacing: .5px; }

  .back-panel { left: 400px; width: 400px; text-align: center; }
  .brand-mark { display: inline-flex; align-items: center; gap: 6px; font-family: "Saira Condensed", sans-serif;
    font-weight: 700; color: var(--brand-blue); text-transform: uppercase; line-height: 1; }
  .brand-mark::before { content: ""; width: 10px; height: 10px; background: var(--brand-blue); }
  .back-panel .brand-mark { margin-top: 150px; font-size: 20px; }
  .contact { position: absolute; left: 0; width: 400px; top: 209px; font-size: 9px; color: #333; line-height: 13px; }
  .contact .web { font-weight: 700; }
  .contact .social span::before { content: ""; display: inline-block; width: 6px; height: 6px;
    background: #333; margin-right: 2px; }

  .cover { left: 800px; width: 400px; }
  .photo-compass { position: absolute; left: 0; top: 0; width: 400px; height: 203px;
    background: radial-gradient(circle at 80% 60%, #f1dfb3 0%, #b88a45 40%, #6a4a22 80%, #3b2812 100%); }
  .cover-bar { position: absolute; left: 66px; top: 205px; width: 334px; height: 22px; background: var(--brand-blue); }
  .cover-title { position: absolute; left: 20px; top: 238px; font-family: "Saira Condensed", sans-serif;
    font-weight: 700; font-size: 42px; color: var(--brand-blue); line-height: 1; letter-spacing: .5px; }
  .cover-tagline { position: absolute; left: 20px; top: 282px; font-size: 14px; letter-spacing: 3.6px; color: #222; }
  .cover .brand-mark { position: absolute; right: 28px; top: 358px; font-size: 18px; }

  /* Inside spread */
  .approach { left: 0; width: 400px; z-index: 2; }
  .section-heading { font-family: "Saira Condensed", sans-serif; font-weight: 700; color: var(--brand-blue);
    font-variant: small-caps; line-height: 1; white-space: nowrap; }
  .approach .section-heading { position: absolute; left: 27px; top: 22px; font-size: 40px; letter-spacing: 1.6px; }
  .approach-copy { position: absolute; left: 27px; top: 63px; width: 360px; height: 232px; columns: 2; column-gap: 12px;
    font-family: "Crimson Pro", serif; font-size: 9.7px; line-height: 10.9px; }
  .approach-copy p { margin-bottom: 10.9px; }
  .pull-banner { position: absolute; left: 0; top: 301px; width: 472px; height: 99px; }
  .pull-banner p { position: absolute; left: 27px; top: 20px; width: 350px; color: #fff; font-size: 14.5px;
    font-weight: 300; line-height: 20px; }

  .photo-insight { left: 400px; width: 397px; z-index: 1;
    background: radial-gradient(ellipse at 45% 30%, #d8c3a0 0%, #7d6240 35%, #2a1f14 70%, #0d0a07 100%); }

  .services { left: 797px; width: 403px; z-index: 2; }
  .insight-banner { position: absolute; left: -37px; top: 0; width: 440px; height: 100px; }
  .insight-banner span { position: absolute; left: 52px; top: 26px; font-family: "Saira Condensed", sans-serif;
    font-weight: 700; font-size: 40px; color: #fff; letter-spacing: .5px; line-height: 1; }
  .services .section-heading { position: absolute; left: 29px; top: 113px; font-size: 38px; letter-spacing: 2.8px; }
  .offer-box { position: absolute; left: 38px; top: 161px; width: 165px; height: 214px; background: var(--brand-blue);
    padding: 4px; box-shadow: 3px 3px 4px rgba(0,0,0,.4); }
  .offer-box-inner { border: 1px solid #fff; height: 100%; padding: 12px 6px 0 8px; color: #fff; }
  .offer h3 { font-weight: 400; font-size: 11px; line-height: 11px; }
  .offer ul { margin: 3px 0 12px 12px; font-size: 6px; line-height: 8px; }
  .services-copy { position: absolute; left: 219px; top: 151px; width: 178px;
    font-family: "Crimson Pro", serif; font-size: 8.7px; line-height: 9.3px; }
  .services-copy p { margin-bottom: 5px; }
</style>
</head>
<body>

<section class="spread spread--outside">
  <div class="panel photo-chess" role="img" aria-label="Sepia photo of a hand moving a king across a chessboard">
    <blockquote class="quote-box">
      <p>Musaperibus audae consed maximus et diti serum volupie nimporiones am, nihil estoriande rem litiumque vollores aut volorem aces rem sequo ipsunt doluptae natios ius nobis am aliatest.</p>
      <p class="author">DANIEL R. HARTLEY, MANAGING DIRECTOR</p>
    </blockquote>
  </div>

  <div class="panel back-panel">
    <div class="brand-mark">Brightwater Advisors</div>
    <div class="contact">
      <div class="web">www.brightwater-advisors.com</div>
      <div>(555) 014-2270 | info@brightwater-advisors.com</div>
      <div class="social"><span>Brightwater-Advisors</span> | <span>@BrightwaterAdv</span> | <span>brightwater-advisors-ltd</span></div>
    </div>
  </div>

  <div class="panel cover">
    <div class="photo-compass" role="img" aria-label="Warm close-up photo of a brass compass on a wooden table"></div>
    <div class="cover-bar"></div>
    <h1 class="cover-title">UNCOMMON INSIGHTS</h1>
    <p class="cover-tagline">Aligning Resources to Opportunity</p>
    <div class="brand-mark">Brightwater Advisors</div>
  </div>
</section>

<section class="spread spread--inside">
  <div class="panel approach">
    <h2 class="section-heading">Approach &amp; Philosophy</h2>
    <div class="approach-copy">
      <p>Like a person, an organization moves at its own rhythm through various development cycles. Sometimes the path followed is not satisfactory anymore. Or the path is even detrimental and it calls for a revolution: a fundamental change in the way of thinking, acting, visualizing, or engaging. An organization must step on a new or emerging path. Those are times of many ideas, challenges, explorations, ambiguity, choices, contradictions, chaos and order. To navigate that time, it requires a strong cross-functional approach, deep functional expertise, and extremely strong change skills. You are not trying to catch up; you want to take quantum steps towards achieving your goals.</p>
      <p>We focus on what helps your organization move. It is that simple. It involves many dimensions and potential approaches. The path is not always easy. Not everyone desires a revolution. It is for those who have struggled to analyze and solve particular problems, or have wrestled with attempting larger jumps towards their goals. For people who know they are tackling something that is not a simple issue with a simple solution, our services may be for you.</p>
      <p>Because of our deep expertise, our consultants are often called in to manage the high risk and high impact projects. We are also often brought in to "save" or turnaround struggling initiatives. Our consultants deliver awareness, clarity, and most importantly, results.</p>
      <p>Contact us to experience the difference of working with Brightwater Advisors</p>
    </div>
    <svg class="pull-banner" viewBox="0 0 472 99" aria-hidden="true">
      <polygon points="0,0 400,0 472,49.5 400,99 0,99" fill="var(--brand-blue)"/>
    </svg>
    <div class="pull-banner"><p>Musaperibus audae consed maximus et diti serum volupie nimporiones am, nihil estoriande rem litiumque vollores aut volorem aces rem sequo ipsunt doluptae natios ius nobis am aliatest.</p></div>
  </div>

  <div class="panel photo-insight" role="img" aria-label="Sepia photo of a businessman reaching toward glowing floating data charts"></div>

  <div class="panel services">
    <svg class="insight-banner" viewBox="0 0 440 100" aria-hidden="true">
      <polygon points="0,0 440,0 440,100 0,100 37,50" fill="var(--brand-blue)"/>
    </svg>
    <div class="insight-banner"><span>UNCOMMON INSIGHTS</span></div>
    <h2 class="section-heading">Our Service Offerings</h2>
    <div class="offer-box">
      <div class="offer-box-inner">
        <div class="offer">
          <h3>Economic Development.</h3>
          <ul><li>Award-Winning Proprietary Approach</li><li>Culture or Values Based Planning</li><li>Stakeholder Agreement, Community Voice</li></ul>
        </div>
        <div class="offer">
          <h3>Feasibility Studies and Site Options Analysis.</h3>
          <ul><li>Comprehensive analysis of current state and options</li><li>Statistical modeling tool creates best fit scenarios</li><li>Strategic planning for current and future use</li></ul>
        </div>
        <div class="offer">
          <h3>Resilience Assessment and Planning.</h3>
          <ul><li>Instilling the agility to capitalize on opportunities</li><li>Not surviving, but thriving during change</li><li>Building awareness on the fringe</li></ul>
        </div>
      </div>
    </div>
    <div class="services-copy">
      <p>Very different from most consulting firms, our focus is on developing strategies and solutions specific to your needs, not just doing what we have done for the last 5 clients.</p>
      <p>We operate by a strict code of ethics and put integrity first in all of our client interactions. In addition, our projects are carried out with the utmost discretion and our clients confidentiality is critical to us being able to drive the type of change that is needed for them to succeed.</p>
      <p>Our solutions are not the single-threaded 'magic bullet' solutions. We do not have a magic technology that will solve all of your organization problems. We know from being there that real change is difficult and it takes work on multiple fronts. Getting the right parts of the organization doing the right things at the right time is not easy and it takes experts in multiple areas who can bring the best the organization has to offer into a holistic solution. Our experts make that kind of change happen for our client every day and we have seen the powerful results it can bring.</p>
    </div>
  </div>
</section>

</body>
</html>
```